velto fulfilment website design wordpress

I'm looking for a website design (WordPress) for an order fulfillment company. the company is a micro-fulfillment company that offers the following services: inventory management, order fulfillment, returns, and storage. the site must have a multilanguage feature.

the website must look modern and professional. Also, the website should not look like it came from a template.

sample site:
https://go-pakmo.nl/fulfilment-tarieven/
https://www.zendrix.com/

Target Market(s)

ecommerce owner

Industry/Entity Type

logistics

Coding

Coded - Design and coding required

Number of Pages Required

5+ page

Colors
0054AA
0677BA
7BADD7
CADEEF
E8F1F8

Requirements
Must have
• multilanguage
Should not have
• look that the design came from a template

```html
<!DOCTYPE html>
<html lang="en">
<head>
<meta charset="utf-8">
<title>Velto Fulfilment</title>
<link href="https://fonts.googleapis.com/css2?family=Nunito:wght@400;600;700;800;900&display=swap" rel="stylesheet">
<style>
:root{
  --navy:#1b3f66;
  --sky:#6aaeea;
  --sky-soft:#6fb2ec;
  --ink:#333a44;
  --muted:#555c66;
  --paper:#ffffff;
  --mist:#f5f3f4;
  --night:#121212;
}
*{box-sizing:border-box;margin:0;padding:0}
html,body{width:1200px;height:3842px;overflow:hidden}
body{position:relative;font-family:'Nunito',sans-serif;color:var(--ink);background:var(--paper)}
.abs{position:absolute}
/* header */
.site-header{position:absolute;left:0;top:0;width:1200px;height:115px;background:var(--paper)}
.brand{position:absolute;display:flex;align-items:center;gap:10px;font-weight:800;color:var(--navy);font-size:21px;letter-spacing:.3px}
.brand-mark{width:26px;height:26px;background:var(--navy)}
.contact-item{position:absolute;top:22px;display:flex;align-items:center;gap:12px}
.contact-item small{display:block;font-size:11px;color:var(--ink)}
.contact-item span{display:block;font-size:16px;color:var(--ink)}
.divider-v{width:1px;height:40px;background:#cfd6de}
.btn{display:inline-block;background:var(--sky);color:#fff;font-weight:700;text-decoration:none;text-align:center}
.cta-start{position:absolute;left:897px;top:24px;width:100px;height:33px;line-height:33px;font-size:15px;font-weight:600}
.lang{position:absolute;left:1007px;top:24px;width:66px;height:33px;border:1px solid var(--sky);font-size:12px;display:flex;align-items:center;justify-content:center;gap:5px}
.flag{width:16px;height:10px;background:linear-gradient(#b22 0 50%,#fff 50% 60%,#b22 60%);position:relative}
.flag::before{content:"";position:absolute;left:0;top:0;width:7px;height:6px;background:#2a3e7a}
.main-nav{position:absolute;top:78px;left:453px;display:flex;gap:28px;font-size:16px}
.main-nav a{color:var(--ink);text-decoration:none}
.main-nav a.active{color:var(--sky)}
/* hero */
.hero{position:absolute;left:0;top:115px;width:1200px;height:524px;background:linear-gradient(90deg,#7b5a3f 0%,#4b4a45 30%,#2e3a4c 55%,#1d2c3f 100%)}
.hero h1{position:absolute;left:622px;top:110px;color:#fff;font-weight:900;font-size:58px;line-height:60px;letter-spacing:1px}
.hero p{position:absolute;left:626px;top:245px;width:440px;color:#fff;font-size:17px;line-height:19px}
.hero .btn{position:absolute;left:628px;top:328px;width:120px;height:44px;line-height:44px;font-size:16px}
.dots{position:absolute;left:560px;top:474px;display:flex;gap:13px}
.dots i{width:12px;height:12px;border-radius:50%;background:#fff}
.dots i.on{background:var(--sky)}
/* headings */
.section-title{position:absolute;font-weight:900;color:var(--navy);text-align:center}
.rule{position:absolute;height:3px;width:48px;background:var(--sky)}
/* services */
.service-card{position:absolute;width:454px;height:217px;background:#fff;box-shadow:0 0 30px rgba(0,0,0,.08)}
.service-icon{position:absolute;left:32px;top:38px;width:98px;height:98px;border-radius:50%;background:var(--navy);display:flex;align-items:center;justify-content:center}
.service-card h3{position:absolute;left:168px;top:28px;font-size:20px;font-weight:600;color:var(--navy)}
.service-card p{position:absolute;left:168px;top:66px;width:250px;font-size:13px;line-height:19px;color:var(--muted)}
.service-card .btn{position:absolute;left:170px;top:153px;width:83px;height:30px;line-height:30px;font-size:11px}
/* welcome */
.welcome{position:absolute;left:0;top:1300px;width:1200px;height:527px;background:linear-gradient(90deg,#8d9db0 0%,#b7c4d3 40%,#d3dce6 70%,#c6d2de 100%)}
.welcome-circle{position:absolute;left:618px;top:48px;width:424px;height:424px;border-radius:50%;background:#fff;text-align:center}
.welcome-circle h2{margin-top:66px;font-size:30px;font-weight:900;color:var(--navy);line-height:34px}
.welcome-circle h2 em{font-style:normal;color:var(--sky)}
.welcome-circle .rule{left:188px;top:153px}
.welcome-circle p{position:absolute;left:46px;top:178px;width:332px;font-size:14px;line-height:19px;color:var(--muted)}
.welcome-circle .btn{position:absolute;left:148px;top:334px;width:120px;height:44px;line-height:44px;font-size:16px}
/* split sections */
.split-title{position:absolute;font-weight:900;font-size:30px;line-height:38px;color:var(--navy)}
.split-title em{font-style:normal;color:var(--sky)}
.split-text{position:absolute;font-size:14px;line-height:18.5px;color:var(--muted)}
.photo{position:absolute}
.rates{position:absolute;left:0;top:2340px;width:1200px;height:582px;background:var(--mist)}
.checklist{position:absolute;left:604px;top:2560px;list-style:none;font-size:17px;color:var(--ink)}
.checklist li{height:37px;display:flex;align-items:center;gap:18px}
.checklist li::before{content:"";border-left:6px solid var(--sky);border-top:5px solid transparent;border-bottom:5px solid transparent}
/* quote */
.quote{position:absolute;left:0;top:2922px;width:1200px;height:535px;background:var(--sky-soft)}
.quote h2{position:absolute;width:1200px;top:62px;text-align:center;color:#fff;font-size:30px;font-weight:900}
.quote .rule{left:577px;top:106px;background:#fff}
.field{position:absolute;background:#fff;font-size:15px;color:var(--muted);padding:20px 18px}
.submit{position:absolute;left:530px;top:444px;width:140px;height:44px;line-height:44px;background:var(--navy);color:#fff;font-weight:800;font-size:17px;text-align:center}
/* footer */
.site-footer{position:absolute;left:0;top:3457px;width:1200px;height:385px;background:var(--night);color:#fff}
.foot-head{position:absolute;top:36px;font-size:14px;font-weight:800}
.foot-head::after{content:"";display:block;margin-top:10px;height:2px;background:#fff}
.foot-item{position:absolute;display:flex;align-items:center;gap:12px;font-size:12px;line-height:15px}
.foot-dot{width:24px;height:24px;border-radius:50%;background:#1f5b92;display:flex;align-items:center;justify-content:center;flex:none}
.foot-menu{position:absolute;left:717px;top:100px;list-style:none;font-size:12px;line-height:19.5px}
.foot-rule{position:absolute;left:133px;top:280px;width:934px;height:1px;background:#ddd}
.copyright{position:absolute;top:335px;width:1200px;text-align:center;font-size:11px}
</style>
</head>
<body>

<header class="site-header">
  <div class="brand" style="left:133px;top:38px"><span class="brand-mark"></span>VELTO FULFILMENT</div>
  <div class="contact-item" style="left:456px">
    <svg width="22" height="16" viewBox="0 0 22 16"><rect width="22" height="16" rx="2" fill="#6aaeea"/><path d="M1 2l10 7 10-7" stroke="#fff" stroke-width="2" fill="none"/></svg>
    <div class="divider-v"></div>
    <div><small>Email us</small><span>info@veltofulfilment.com</span></div>
  </div>
  <div class="contact-item" style="left:708px">
    <svg width="22" height="22" viewBox="0 0 24 24"><path d="M6.6 10.8a15 15 0 006.6 6.6l2.2-2.2c.3-.3.7-.4 1-.2 1.1.4 2.3.6 3.6.6.6 0 1 .4 1 1V20c0 .6-.4 1-1 1A17 17 0 013 4c0-.6.4-1 1-1h3.5c.6 0 1 .4 1 1 0 1.3.2 2.5.6 3.6.1.3 0 .7-.2 1z" fill="#6aaeea"/></svg>
    <div class="divider-v"></div>
    <div><small>Call us</small><span>+1 555 010 0199</span></div>
  </div>
  <a class="btn cta-start">Get Started</a>
  <div class="lang"><span class="flag"></span>EN ▾</div>
  <nav class="main-nav">
    <a class="active">Home</a><a>About Us</a><a>Fulfillment solutions</a><a>Services</a><a>Rates</a><a>Blog</a><a>Contact</a>
  </nav>
</header>

<section class="hero" role="img" aria-label="Warehouse worker in hard hat and safety vest walking between stocked shelves">
  <h1>INVENTORY<br>MANAGEMENT</h1>
  <p>Lorem ipsum dolor sit amet, consectetur adipiscing elit, sed do eiusmod tempor incididunt ut labore et dolore magna aliqua. Ut enim ad minim veniam</p>
  <a class="btn">Read More</a>
  <div class="dots"><i></i><i class="on"></i><i></i></div>
</section>

<h2 class="section-title" style="left:0;top:680px;width:1200px;font-size:32px">OUR SERVICES</h2>
<div class="rule" style="left:576px;top:738px"></div>

<article class="service-card" style="left:133px;top:788px">
  <div class="service-icon"><svg width="52" height="52" viewBox="0 0 52 52" fill="none" stroke="#fff" stroke-width="2.5"><path d="M18 10l8-4 8 4v9l-8 4-8-4z"/><path d="M6 24v12l10 10M46 24v12L36 46M14 30l6 8M38 30l-6 8"/></svg></div>
  <h3>Inventory Management</h3>
  <p>Lorem ipsum dolor sit amet, conse ctet ur adipiscing elit, sed do eiusmod tem por incididunt ut labore et dolore magna aliqua.</p>
  <a class="btn">Read More</a>
</article>
<article class="service-card" style="left:615px;top:788px">
  <div class="service-icon"><svg width="52" height="52" viewBox="0 0 52 52" fill="none" stroke="#fff" stroke-width="2.5"><rect x="10" y="8" width="28" height="34" rx="2"/><path d="M16 16h16M16 24h10M6 46h40"/><rect x="30" y="26" width="14" height="12"/></svg></div>
  <h3>Order Fulfillment</h3>
  <p>Lorem ipsum dolor sit amet, conse ctet ur adipiscing elit, sed do eiusmod tem por incididunt ut labore et dolore magna aliqua.</p>
  <a class="btn">Read More</a>
</article>
<article class="service-card" style="left:133px;top:1031px">
  <div class="service-icon"><svg width="52" height="52" viewBox="0 0 52 52" fill="none" stroke="#fff" stroke-width="2.5"><rect x="8" y="20" width="26" height="24"/><path d="M8 28h26M28 10a10 10 0 0110 10v4M34 16l4 4 4-4"/></svg></div>
  <h3>Returns</h3>
  <p>Lorem ipsum dolor sit amet, conse ctet ur adipiscing elit, sed do eiusmod tem por incididunt ut labore et dolore magna aliqua.</p>
  <a class="btn">Read More</a>
</article>
<article class="service-card" style="left:615px;top:1031px">
  <div class="service-icon"><svg width="52" height="52" viewBox="0 0 52 52"><path d="M4 20L26 6l22 14v26H4z" fill="#fff"/><g fill="#1b3f66"><rect x="10" y="24" width="9" height="7"/><rect x="22" y="24" width="9" height="7"/><rect x="34" y="24" width="9" height="7"/><rect x="10" y="34" width="9" height="7"/><rect x="22" y="34" width="9" height="7"/><rect x="34" y="34" width="9" height="7"/></g></svg></div>
  <h3>Storage</h3>
  <p>Lorem ipsum dolor sit amet, conse ctet ur adipiscing elit, sed do eiusmod tem por incididunt ut labore et dolore magna aliqua.</p>
  <a class="btn">Read More</a>
</article>

<section class="welcome" role="img" aria-label="Woman packing an order box at a desk in a bright studio">
  <div class="welcome-circle">
    <h2>WELCOME TO<br><em>VELTO FULFILMENT</em></h2>
    <div class="rule"></div>
    <p>Sed ut perspiciatis unde omnis iste natus error sit voluptatem accusantium doloremque laudantium, totam rem aperiam, eaque ipsa quae ab illo inventore veritatis et quasi architecto beatae vitae dicta sunt explicabo. Nemo enim ipsam voluptatem quia voluptas sit aspernatur aut odit aut fugit</p>
    <a class="btn">Read More</a>
  </div>
</section>

<h2 class="split-title" style="left:133px;top:1928px">FULFILMENT SERVICES<br><em>FOR STARTUPS &amp; SMES</em></h2>
<div class="rule" style="left:134px;top:2028px"></div>
<p class="split-text" style="left:134px;top:2060px;width:346px">Sed ut perspiciatis unde omnis iste natus error sit voluptatem accusantium doloremque laudantium, totam rem aperiam, eaque ipsa quae ab illo inve ntore veritatis et quasi architecto beatae vitae dicta sunt explicabo. Nemo enim ipsam voluptatem quia voluptas sit aspernatur aut odit aut fugit</p>
<a class="btn abs" style="left:134px;top:2195px;width:121px;height:44px;line-height:44px;font-size:16px">Read More</a>
<div class="photo" style="left:527px;top:1875px;width:543px;height:403px;background:linear-gradient(135deg,#b89a78,#8a6f55 45%,#3d4658)" role="img" aria-label="Businesswoman reviewing a tablet in front of warehouse shelves"></div>

<section class="rates"></section>
<div class="photo" style="left:131px;top:2391px;width:412px;height:485px;background:linear-gradient(160deg,#c8c4bf,#b48f68 45%,#9b8a78 75%,#6d6a68)" role="img" aria-label="Workers in hard hats checking stock at warehouse shelving with laptop"></div>
<h2 class="split-title" style="left:598px;top:2388px">ALL-IN FULFILLMENT RATES<br>FOR STOCKING, <em>ORDER PICKING<br>AND SHIPPING!</em></h2>
<div class="rule" style="left:599px;top:2522px"></div>
<ul class="checklist">
  <li>Goods receipt</li><li>Taking in your goods</li><li>Inventory management</li><li>Order processing</li><li>Packing material</li><li>Real-time inventory management and Track</li><li>Use of our customer portal</li>
</ul>
<a class="btn abs" style="left:600px;top:2833px;width:121px;height:44px;line-height:44px;font-size:16px">Read More</a>

<section class="quote">
  <h2>REQUEST A QUOTE</h2>
  <div class="rule"></div>
  <div class="field" style="left:238px;top:143px;width:356px;height:48px;padding-top:15px">Name</div>
  <div class="field" style="left:607px;top:143px;width:356px;height:48px;padding-top:15px">Email</div>
  <div class="field" style="left:238px;top:206px;width:356px;height:48px;padding-top:15px">Phone No</div>
  <div class="field" style="left:607px;top:206px;width:356px;height:48px;padding-top:15px">Subject</div>
  <div class="field" style="left:238px;top:270px;width:726px;height:146px;padding-top:15px">Message</div>
  <div class="submit">SUBMIT</div>
</section>

<footer class="site-footer">
  <div class="brand" style="left:131px;top:160px;color:#1f5b92"><span class="brand-mark" style="background:#1f5b92"></span>VELTO FULFILMENT</div>

  <div class="foot-head" style="left:404px;width:192px">CONTACT US</div>
  <div class="foot-item" style="left:404px;top:108px"><span class="foot-dot"><svg width="10" height="13" viewBox="0 0 10 13"><path d="M5 0a5 5 0 015 5c0 4-5 8-5 8S0 9 0 5a5 5 0 015-5z" fill="#fff"/><circle cx="5" cy="5" r="2" fill="#1f5b92"/></svg></span><span>48 Harbour Lane, Northfield,<br>ON A1B 2C3, Canada</span></div>
  <div class="foot-item" style="left:404px;top:158px"><span class="foot-dot"><svg width="12" height="12" viewBox="0 0 24 24"><path d="M6.6 10.8a15 15 0 006.6 6.6l2.2-2.2c.3-.3.7-.4 1-.2 1.1.4 2.3.6 3.6.6.6 0 1 .4 1 1V20c0 .6-.4 1-1 1A17 17 0 013 4c0-.6.4-1 1-1h3.5c.6 0 1 .4 1 1 0 1.3.2 2.5.6 3.6.1.3 0 .7-.2 1z" fill="#fff"/></svg></span><span>Call Us<br>+1 555 010 0199</span></div>
  <div class="foot-item" style="left:404px;top:210px"><span class="foot-dot"><svg width="12" height="9" viewBox="0 0 22 16"><rect width="22" height="16" fill="#fff"/><path d="M1 2l10 7 10-7" stroke="#1f5b92" stroke-width="2" fill="none"/></svg></span><span>E mail Us<br>info@veltofulfilment.com</span></div>

  <div class="foot-head" style="left:716px;width:110px">MENU</div>
  <ul class="foot-menu"><li>Home</li><li>About Us</li><li>Fulfillment solutions</li><li>Services</li><li>Rates</li><li>Blog</li><li>Contact</li></ul>

  <div class="foot-head" style="left:963px;width:107px">FOLLOW US</div>
  <div class="foot-item" style="left:962px;top:112px"><span class="foot-dot"></span><span>Like us on<br>FRIENDLINK</span></div>
  <div class="foot-item" style="left:962px;top:162px"><span class="foot-dot"></span><span>Follow us on<br>CHIRPER</span></div>
  <div class="foot-item" style="left:962px;top:212px"><span class="foot-dot"></span><span>Follow us on<br>CLIPTOK</span></div>

  <div class="foot-rule"></div>
  <p class="copyright">Copyright © 2023 All Rights Reserved</p>
</footer>

</body>
</html>
```